Business Card Design Template

I have a software development and managed services company. My target market is mid market and government. I need a business card design template where I can make changes to contact information to send to print. I want the look and feel to be towards todays technology.

```html
<!DOCTYPE html>
<html lang="en">
<head>
<meta charset="utf-8">
<title>Business Card Template</title>
<link rel="stylesheet" href="https://fonts.googleapis.com/css2?family=Open+Sans:wght@400;600;700&display=swap">
<style>
  :root {
    --backdrop: #2f3439;
    --card-white: #ffffff;
    --accent: #ef5129;
    --accent-light: #f4683a;
    --ink: #1f1f1f;
    --muted: #6b6b6b;
    --rule: #c9c9c9;
  }
  * { box-sizing: border-box; margin: 0; padding: 0; }
  html, body {
    width: 1200px; height: 900px; overflow: hidden;
    background: var(--backdrop);
    font-family: "Open Sans", Arial, sans-serif;
  }
  .canvas { position: relative; width: 1200px; height: 900px; }
  .card {
    position: absolute; width: 520px; height: 300px;
    border-radius: 22px; overflow: hidden;
  }
  /* Front */
  .card-front { left: 70px; top: 480px; background: var(--card-white); }
  .brand {
    position: absolute; left: 272px; top: 52px;
    display: flex; align-items: center; gap: 12px;
  }
  .brand-mark { width: 30px; height: 30px; background: var(--accent); }
  .brand-name {
    font-size: 22px; font-weight: 400; letter-spacing: 1.5px;
    color: var(--ink);
  }
  .identity {
    position: absolute; right: 280px; top: 128px; text-align: right;
  }
  .identity-name { font-size: 27px; font-weight: 400; color: var(--accent); line-height: 1.1; }
  .identity-title { font-size: 13px; color: var(--muted); margin-bottom: 8px; }
  .identity-address { font-size: 13px; color: var(--ink); line-height: 1.35; }
  .divider {
    position: absolute; left: 258px; top: 132px; width: 1px; height: 112px;
    background: var(--rule);
  }
  .contacts {
    position: absolute; left: 274px; top: 132px; list-style: none;
  }
  .contact {
    display: flex; align-items: center; gap: 10px;
    font-size: 14px; color: var(--ink); height: 28px;
  }
  .contact svg { width: 15px; height: 15px; flex: none; }
  /* Back */
  .card-back {
    left: 610px; top: 130px;
    background: linear-gradient(135deg, var(--accent) 0%, var(--accent-light) 100%);
    color: #fff;
  }
  .slogan {
    position: absolute; left: 50%; top: 50%; transform: translate(-50%, -50%);
    width: 250px;
  }
  .slogan-small { font-size: 16px; font-weight: 400; line-height: 1; }
  .slogan-big { font-size: 34px; font-weight: 600; letter-spacing: 1px; line-height: 1.05; }
  .slogan-line-1 { display: flex; align-items: flex-end; gap: 6px; }
  .slogan-line-2 { display: flex; align-items: flex-end; gap: 6px; margin-top: 6px; justify-content: flex-end; }
  .slogan-rule { height: 2px; background: #fff; margin: 8px 0 6px; }
  .slogan-brand { text-align: right; font-size: 36px; font-weight: 700; letter-spacing: 1px; line-height: 1; }
</style>
</head>
<body>
<main class="canvas">

  <section class="card card-back" aria-label="Card back">
    <div class="slogan">
      <div class="slogan-line-1">
        <span class="slogan-small">our</span>
        <span class="slogan-big">PRODUCTS</span>
      </div>
      <div class="slogan-rule"></div>
      <div class="slogan-line-2">
        <span class="slogan-small">are our</span>
        <span class="slogan-brand">BRAND</span>
      </div>
    </div>
  </section>

  <section class="card card-front" aria-label="Card front">
    <div class="brand">
      <span class="brand-mark"></span>
      <span class="brand-name">MERIDIAN WORKS</span>
    </div>

    <div class="identity">
      <p class="identity-name">Dana Whitfield</p>
      <p class="identity-title">President</p>
      <p class="identity-address">18 Alder Ave.<br>Fairview, NY 10520</p>
    </div>

    <div class="divider"></div>

    <ul class="contacts">
      <li class="contact">
        <svg viewBox="0 0 16 16"><path fill="var(--accent)" d="M3.5 1.5l2.5 0 1 3.5-1.6 1.2a8 8 0 0 0 4.4 4.4L11 9l3.5 1v2.5a1.5 1.5 0 0 1-1.5 1.5A11.5 11.5 0 0 1 2 3a1.5 1.5 0 0 1 1.5-1.5z"/></svg>
        555.014.2270
      </li>
      <li class="contact">
        <svg viewBox="0 0 16 16"><path fill="var(--accent)" d="M1 7.5L15 1l-4 14-3.2-5.4L1 7.5z"/></svg>
        dana@meridianworks.com
      </li>
      <li class="contact">
        <svg viewBox="0 0 16 16"><circle cx="8" cy="8" r="7" fill="var(--accent)"/></svg>
        danaworks204
      </li>
      <li class="contact">
        <svg viewBox="0 0 16 16"><g fill="none" stroke="var(--accent)" stroke-width="1.4"><circle cx="8" cy="8" r="6.5"/><ellipse cx="8" cy="8" rx="2.8" ry="6.5"/><path d="M1.5 8h13"/></g></svg>
        www.meridianworks.com
      </li>
    </ul>
  </section>

</main>
</body>
</html>
```